We would like a business card that includes our logo on the front and the following information on the back:

Warren Pike, Owner
Phone: (555) 614-0827
email: wpikefencing@brookmail.example

Wally Pike & Sons Fencing provides the following services:
Barbed wire
Smooth wire
High tensile
Electric

On the bottom of the card please add:
Please call or email Warren for estimates.

```html
<!DOCTYPE html>
<html lang="en">
<head>
<meta charset="utf-8">
<title>Wally Pike &amp; Sons Fencing — Business Card</title>
<link rel="stylesheet" href="https://fonts.googleapis.com/css2?family=Montserrat:wght@400;500;700&family=Oswald:wght@500&display=swap">
<style>
  :root {
    --backdrop: #3a3a3a;
    --card: #ffffff;
    --brown: #8a5a3b;
    --ink: #2a2222;
  }
  * { box-sizing: border-box; margin: 0; padding: 0; }
  html, body {
    width: 1200px; height: 1200px; overflow: hidden;
    background: var(--backdrop);
  }
  .card {
    position: absolute;
    left: 250px;
    width: 700px; height: 400px;
    background: var(--card);
    border-radius: 34px;
    overflow: hidden;
  }
  .card--back { top: 150px; }
  .card--front { top: 650px; }

  /* Wordmark: plain set name in the card's text face */
  .wordmark {
    position: absolute;
    font-family: "Montserrat", sans-serif; font-weight: 500;
    color: var(--ink); text-align: center; line-height: 1.25;
    text-transform: uppercase; letter-spacing: 1px;
  }
  .card--back .wordmark { right: 40px; top: 50px; width: 300px; font-size: 22px; }
  .card--front .wordmark { left: 0; right: 0; top: 160px; font-size: 38px; }

  /* Contact block */
  .contact {
    position: absolute; left: 60px; top: 110px;
    font-family: "Montserrat", sans-serif;
    color: var(--ink);
  }
  .contact__header {
    border-left: 7px solid var(--brown);
    padding-left: 12px;
    margin-bottom: 14px;
  }
  .contact__name {
    font-weight: 700; font-size: 38px; line-height: 1;
    color: var(--brown); letter-spacing: 0.5px;
  }
  .contact__title { font-size: 17px; font-weight: 500; line-height: 1.2; }
  .contact__line {
    display: flex; align-items: center; gap: 12px;
    font-size: 21px; line-height: 1.3; margin: 4px 0 0 20px;
  }
  .contact__line svg { width: 20px; height: 20px; fill: var(--brown); flex: none; }

  /* Services */
  .services {
    position: absolute; left: 0; right: 0; top: 268px;
    font-family: "Oswald", sans-serif; text-transform: uppercase;
    text-align: center;
  }
  .services__intro { font-size: 16px; color: var(--ink); margin-bottom: 4px; padding-left: 160px; }
  .services__band {
    background: var(--brown); color: #fff;
    font-size: 21px; letter-spacing: 0.5px; line-height: 1.3;
    padding: 2px 0 2px 160px;
  }

  /* Bottom strip */
  .estimate-band {
    position: absolute; left: 0; right: 0; bottom: 14px; height: 32px;
    background: var(--brown); color: #fff;
    font-family: "Montserrat", sans-serif; font-weight: 500; font-size: 15px;
    display: flex; align-items: center; justify-content: center;
    letter-spacing: 0.3px;
  }
</style>
</head>
<body>
  <section class="card card--back" aria-label="Card back">
    <div class="wordmark">Wally Pike &amp; Sons<br>Fencing</div>

    <div class="contact">
      <div class="contact__header">
        <div class="contact__name">WARREN PIKE</div>
        <div class="contact__title">OWNER</div>
      </div>
      <div class="contact__line">
        <svg viewBox="0 0 24 24" aria-hidden="true"><path d="M6.6 10.8a15.1 15.1 0 0 0 6.6 6.6l2.2-2.2c.3-.3.7-.4 1-.2 1.1.4 2.3.6 3.6.6.6 0 1 .4 1 1V20c0 .6-.4 1-1 1A17 17 0 0 1 3 4c0-.6.4-1 1-1h3.5c.6 0 1 .4 1 1 0 1.3.2 2.5.6 3.6.1.3 0 .7-.2 1z"/></svg>
        <span>(555) 614-0827</span>
      </div>
      <div class="contact__line">
        <svg viewBox="0 0 24 24" aria-hidden="true"><path d="M2 5h20v14H2zm2 2v.5l8 5 8-5V7zm0 2.8V17h16V9.8l-8 5z"/></svg>
        <span>wpikefencing@brookmail.example</span>
      </div>
    </div>

    <div class="services">
      <div class="services__intro">Wally Pike &amp; Sons Fencing provides the following services:</div>
      <div class="services__band">Barbed wire | Smooth wire | High tensile | Electric</div>
    </div>

    <div class="estimate-band">Please call or email Warren for estimates.</div>
  </section>

  <section class="card card--front" aria-label="Card front">
    <div class="wordmark">Wally Pike &amp; Sons<br>Fencing</div>
  </section>
</body>
</html>
```